Djent/ Neoclassical band needs album cover

This album is going to be for an EP that will consist of a bunch of singles released about a month apart from each other. The band is called Brim.sel and the EP title will tentatively be called Velvet Orchards, but I will probably replace the text for each song on the album cover and upload it that way.

It's mostly female ethereal sounding vocals with male rough singing and screaming. Heavy metal drums with some melodic interludes and electronic components as well.

The biggest thing is I'm going to need to redo the album cover so that it changes ever so slightly from cover to cover. If you want an example of what I'm talking about, you can check out my other band Copper Lantern Yard. I took a cover from Pixel hive and imposed different colors over it so that It made each single different while still feeling like a cohesive effort on one project. So either the cover will have to be flexible enough for me to adjust, or you can create 4 different simple covers.

I have no restrictions on subject material. I like nature, geometric designs, modern looking metal covers. The only thing I don't like would be anything slated towards violence, blood, satanic sacrifices, we are not that kind of metal band haha.

I realize a lot of people are creating designs based on the images that I posted. I don't want a door or that style of album cover, I was only posting that to show you how I created 4 different album covers from one design. I don't want the same design for an album cover, or anything even close since I already have a band with that cover.

Designs look the same

Males 18-40

• Easily manipulated design or 4 slightly different designs.
• Violence

```html
<!DOCTYPE html>
<html lang="en">
<head>
<meta charset="utf-8">
<title>Brim.sel – Velvet Orchards single covers</title>
<link rel="stylesheet" href="https://fonts.googleapis.com/css2?family=Inter:wght@400&display=swap">
<style>
  :root {
    --canvas-bg: #f4f5fc;
    --mark: #ffffff;
    --crimson-deep: #8e0c22;
    --crimson-mid: #c8234a;
    --crimson-foam: #f6a6bd;
    --mono-dark: #2b2b2b;
    --mono-mid: #6d6d6d;
    --mono-mist: #cfcfcf;
    --indigo-deep: #0b0f4a;
    --indigo-bright: #2f4fe0;
    --violet: #7b34e6;
  }
  * { box-sizing: border-box; margin: 0; padding: 0; }
  html, body {
    width: 1200px;
    height: 480px;
    overflow: hidden;
    background: var(--canvas-bg);
    font-family: "Inter", sans-serif;
  }
  .cover-series {
    position: relative;
    width: 1200px;
    height: 480px;
  }
  .cover {
    position: absolute;
    top: 68px;
    width: 345px;
    height: 345px;
    overflow: hidden;
    box-shadow: 0 2px 6px rgba(40, 40, 80, 0.12);
  }
  .cover--surf { left: 52px; }
  .cover--ridge { left: 428px; }
  .cover--leaves { left: 803px; }
  .cover__photo {
    position: absolute;
    inset: 0;
  }
  .cover--surf .cover__photo {
    background:
      radial-gradient(circle at 75% 40%, var(--crimson-foam) 0%, transparent 55%),
      linear-gradient(100deg, var(--crimson-deep) 0%, var(--crimson-mid) 45%, var(--crimson-foam) 70%, var(--crimson-mid) 100%);
  }
  .cover--ridge .cover__photo {
    background:
      radial-gradient(ellipse at 50% 35%, var(--mono-mist) 0%, transparent 60%),
      linear-gradient(180deg, var(--mono-mid) 0%, var(--mono-mist) 40%, var(--mono-dark) 100%);
  }
  .cover--leaves .cover__photo {
    background:
      radial-gradient(circle at 65% 25%, var(--indigo-bright) 0%, transparent 55%),
      linear-gradient(180deg, var(--indigo-bright) 0%, var(--indigo-deep) 50%, var(--violet) 100%);
  }
  .cover__mark {
    position: absolute;
    inset: 0;
    width: 100%;
    height: 100%;
  }
  .cover__mark path { fill: var(--mark); }
</style>
</head>
<body>
  <main class="cover-series">
    <section class="cover cover--surf">
      <div class="cover__photo" role="img" aria-label="Aerial photo of surf and foam over dark rocks, tinted crimson and pink"></div>
      <svg class="cover__mark" viewBox="0 0 740 740" aria-hidden="true">
        <path fill-rule="evenodd" d="M370 160L552 265V475L370 580L188 475V265Z M370 226L495 298V442L370 514L245 442V298Z"/>
      </svg>
    </section>
    <section class="cover cover--ridge">
      <div class="cover__photo" role="img" aria-label="Black and white photo of forested mountain ridges in mist"></div>
      <svg class="cover__mark" viewBox="0 0 740 740" aria-hidden="true">
        <path fill-rule="evenodd" d="M370 160L552 265V475L370 580L188 475V265Z M370 226L495 298V442L370 514L245 442V298Z"/>
      </svg>
    </section>
    <section class="cover cover--leaves">
      <div class="cover__photo" role="img" aria-label="Close-up photo of curled leaves, tinted blue fading to violet"></div>
      <svg class="cover__mark" viewBox="0 0 740 740" aria-hidden="true">
        <path fill-rule="evenodd" d="M370 160L552 265V475L370 580L188 475V265Z M370 226L495 298V442L370 514L245 442V298Z"/>
      </svg>
    </section>
  </main>
</body>
</html>
```